U.S. based testing, inspection, and certification (TIC) company needs a new social media design.

We need a social media design primarily for LinkedIn 1200x1200px for our U.S. based company with international capabilities for performing dozens if not hundreds of testing, inspection, and certification (TIC) services. Our primary services include calibration, chemical analysis, consulting engineering, environmental simulation, forensic engineering, materials testing, mechanical testing, and nondestructive testing. Industries we serve are aerospace/aviation, automotive, chemical, commercial properties, construction, consumer products, defense, energy storage, healthcare, insurance/legal, life science, manufacturing, oil & gas, power generation, pulp & paper, and telecommunications. https://corvintest.example/

Guideline hex colors (primary, secondary): #29aae2, #0b1f3b

The final design should communicate:
1. Trust, Integrity, and Independence
2. Technical Expertise and Accuracy
3. Efficiency and Speed
4. Value-Added Partnership

We previously used a hexagon design that we would like to part ways from; hexagon examples and QVR logos uploaded.

```html
<!DOCTYPE html>
<html lang="en">
<head>
<meta charset="utf-8">
<title>QVR – Confidence to Certainty</title>
<link href="https://fonts.googleapis.com/css2?family=Montserrat:wght@700&family=Roboto:wght@400;700&display=swap" rel="stylesheet">
<style>
  :root {
    --navy: #0b1f3b;
    --navy-deep: #0c1d38;
    --navy-low: #123e66;
    --sky: #29aae2;
    --white: #ffffff;
    --plane-tone: rgba(214, 218, 226, 0.32);
  }
  * { margin: 0; padding: 0; box-sizing: border-box; }
  html, body {
    width: 1200px;
    height: 1200px;
    overflow: hidden;
    background: var(--white);
  }
  .canvas {
    position: relative;
    width: 1200px;
    height: 1200px;
    background: var(--white);
  }
  .panel {
    position: absolute;
    left: 94px;
    top: 97px;
    width: 1016px;
    height: 1016px;
    overflow: hidden;
    background: linear-gradient(180deg, var(--navy-deep) 0%, var(--navy) 42%, var(--navy-low) 78%, #0f2d52 100%);
  }
  .spotlight {
    position: absolute;
    inset: 0;
    filter: blur(45px);
  }
  .spotlight-beam {
    position: absolute;
    inset: 0;
    clip-path: polygon(835px 70px, 950px 70px, 1010px 420px, 1000px 960px, 620px 960px, 700px 420px);
    background: linear-gradient(180deg, rgba(41,170,226,0.35) 0%, rgba(41,170,226,0.85) 38%, rgba(41,170,226,0.75) 70%, rgba(41,170,226,0) 100%);
  }
  .brand {
    position: absolute;
    left: 85px;
    top: 82px;
    color: var(--white);
    font-family: "Roboto", Arial, sans-serif;
    font-weight: 700;
  }
  .brand-name {
    font-size: 74px;
    line-height: 0.9;
    letter-spacing: 6px;
  }
  .brand-sub {
    font-size: 15px;
    margin-top: 6px;
  }
  .headline {
    position: absolute;
    left: 85px;
    top: 222px;
    color: var(--white);
    font-family: "Montserrat", Arial, sans-serif;
    font-weight: 700;
    font-size: 54px;
    line-height: 66px;
    white-space: nowrap;
  }
  .lead {
    position: absolute;
    left: 85px;
    top: 450px;
    color: var(--white);
    font-family: "Montserrat", Arial, sans-serif;
    font-weight: 700;
    font-size: 23.5px;
    line-height: 29.5px;
    white-space: nowrap;
  }
  .aircraft {
    position: absolute;
    left: 100px;
    top: 493px;
    width: 815px;
    height: 410px;
    background: radial-gradient(closest-side, var(--plane-tone) 0%, rgba(214,218,226,0.18) 55%, rgba(214,218,226,0) 100%);
    transform: rotate(-22deg);
  }
</style>
</head>
<body>
  <div class="canvas">
    <section class="panel">
      <div class="spotlight"><div class="spotlight-beam"></div></div>
      <div class="brand">
        <div class="brand-name">QVR</div>
        <div class="brand-sub">Corvin Technical Services</div>
      </div>
      <h1 class="headline">We Take<br>You From<br>Confidence to Certainty</h1>
      <p class="lead">Our calibration avionics experts offers LCD<br>display upgrades for Vantor GLS-810 and GLS-810-2<br>ground stations simulators.</p>
      <div class="aircraft" role="img" aria-label="White passenger jet with navy tail climbing to the upper right"></div>
    </section>
  </div>
</body>
</html>
```